Facial Tissue Brand Logo and Design

We would like you to design a Logo for the Facial Tissue Brand "Velora" along with the box design. The pack should indicate the pack size (150 x 2 ply). Also our company logo should be present (attached) along with a barcode. The box size dimensions should be 210mm (L) x 110mm (W) x 70mm (H). We are open to all kinds of nice designs which are attractive but not overdone. Happy designing!

UPDATE:
We appreciate the designs so far... but would also love to see more options in a simple and elegent design style that would look good on a table... please see attached below links for reference purpose:

www.pixmarrow.com/image-photo/cleaning-wipes-isolated-on-white-480215736

www.pixmarrow.com/image-photo/cleaning-wipes-isolated-on-white-692048153

www.pixmarrow.com/image-photo/delicate-female-hands-pulling-tissue-out-2875013649

Happy desgining!

We appreciate the designs so far.. but would like to to see some more options.

```html
<!DOCTYPE html>
<html lang="en">
<head>
<meta charset="UTF-8">
<title>Velora – Tissue Box Panels</title>
<link href="https://fonts.googleapis.com/css2?family=Marcellus&display=swap" rel="stylesheet">
<style>
  :root {
    --bg: #eceeef;
    --paper: #f7f8f8;
    --navy: #1c416c;
    --ink: #15314f;
    --mid-blue: #4b80ae;
    --pale-blue: #acc0c6;
    --seam: #2a2f35;
  }
  * { margin: 0; padding: 0; box-sizing: border-box; }
  html, body {
    width: 1200px;
    height: 675px;
    overflow: hidden;
    background: var(--bg);
    font-family: "Marcellus", serif;
    color: var(--ink);
  }
  .canvas {
    position: relative;
    width: 1200px;
    height: 675px;
  }
  .panel {
    position: absolute;
    background: var(--paper);
    overflow: hidden;
  }
  .panel--top   { left: 190px; top: 50px;  width: 700px; height: 340px; }
  .panel--front { left: 190px; top: 390px; width: 700px; height: 230px; border-top: 2px solid var(--seam); }
  .panel--side  { left: 890px; top: 300px; width: 210px; height: 320px; border-left: 2px solid var(--seam); }

  .leaf-field {
    position: absolute;
    inset: 0;
    background:
      radial-gradient(ellipse 30% 45% at 4% 40%, rgba(75,128,174,.55), transparent 70%),
      radial-gradient(ellipse 30% 35% at 45% 5%, rgba(172,192,198,.6), transparent 70%),
      radial-gradient(ellipse 18% 40% at 94% 20%, rgba(28,65,108,.5), transparent 70%),
      radial-gradient(ellipse 22% 40% at 88% 90%, rgba(75,128,174,.5), transparent 70%),
      radial-gradient(ellipse 22% 30% at 25% 95%, rgba(172,192,198,.5), transparent 70%),
      var(--paper);
  }
  .panel--front .leaf-field {
    background:
      radial-gradient(ellipse 15% 45% at 8% 90%, rgba(28,65,108,.45), transparent 70%),
      radial-gradient(ellipse 14% 45% at 30% 45%, rgba(75,128,174,.45), transparent 70%),
      radial-gradient(ellipse 24% 60% at 82% 60%, rgba(172,192,198,.55), transparent 70%),
      var(--paper);
  }
  .panel--side .leaf-field {
    background:
      radial-gradient(ellipse 40% 30% at 70% 20%, rgba(28,65,108,.45), transparent 70%),
      radial-gradient(ellipse 35% 40% at 95% 75%, rgba(75,128,174,.5), transparent 70%),
      radial-gradient(ellipse 40% 20% at 35% 85%, rgba(172,192,198,.5), transparent 70%),
      var(--paper);
  }

  .count-badge {
    position: absolute;
    border-radius: 50%;
    background: var(--navy);
    color: #fff;
    display: flex;
    flex-direction: column;
    align-items: center;
    justify-content: center;
    line-height: 1;
  }
  .count-badge__number { font-size: 22px; }
  .count-badge__label  { font-size: 7px; margin-top: 4px; letter-spacing: .5px; }
  .panel--top .count-badge   { left: 30px; top: 30px; width: 54px; height: 66px; border-radius: 27px; }
  .panel--front .count-badge { left: 28px; top: 28px; width: 52px; height: 62px; border-radius: 26px; }

  .brand {
    position: absolute;
    left: 0; right: 0;
    text-align: center;
  }
  .brand__name {
    display: inline-flex;
    align-items: center;
    gap: 14px;
    color: var(--ink);
    letter-spacing: 4px;
  }
  .brand__dot {
    border-radius: 50%;
    background: var(--mid-blue);
  }
  .brand__tagline {
    display: block;
    color: var(--ink);
    text-transform: uppercase;
  }
  .panel--top .brand { top: 120px; }
  .panel--top .brand__name { font-size: 64px; }
  .panel--top .brand__dot { width: 22px; height: 22px; }
  .panel--top .brand__tagline { font-size: 12px; letter-spacing: 7px; margin-top: 34px; }

  .panel--front .brand { top: 70px; }
  .panel--front .brand__name { font-size: 36px; }
  .panel--front .brand__dot { width: 13px; height: 13px; gap: 8px; }
  .panel--front .brand__tagline { font-size: 8px; letter-spacing: 5px; margin-top: 22px; }

  .side-brand {
    position: absolute;
    left: 105px;
    top: 160px;
    transform: translate(-50%, -50%) rotate(90deg);
    white-space: nowrap;
    text-align: center;
  }
  .side-brand .brand__name { font-size: 28px; gap: 8px; }
  .side-brand .brand__dot { width: 10px; height: 10px; }
  .side-brand .brand__tagline { font-size: 6px; letter-spacing: 4px; margin-top: 10px; }
</style>
</head>
<body>
<main class="canvas">
  <section class="panel panel--top">
    <div class="leaf-field" role="img" aria-label="Scattered leaf pattern in navy, mid blue and pale grey-blue"></div>
    <div class="count-badge"><span class="count-badge__number">150</span><span class="count-badge__label">TISSUES</span></div>
    <div class="brand">
      <span class="brand__name"><span class="brand__dot"></span>Velora</span>
      <span class="brand__tagline">Premium Soft Tissues</span>
    </div>
  </section>

  <section class="panel panel--front">
    <div class="leaf-field" role="img" aria-label="Scattered leaf pattern in navy, mid blue and pale grey-blue"></div>
    <div class="count-badge"><span class="count-badge__number">150</span><span class="count-badge__label">TISSUES</span></div>
    <div class="brand">
      <span class="brand__name"><span class="brand__dot"></span>Velora</span>
      <span class="brand__tagline">Premium Soft Tissues</span>
    </div>
  </section>

  <section class="panel panel--side">
    <div class="leaf-field" role="img" aria-label="Scattered leaf pattern in navy, mid blue and pale grey-blue"></div>
    <div class="side-brand">
      <span class="brand__name"><span class="brand__dot"></span>Velora</span>
      <span class="brand__tagline">Premium Soft Tissues</span>
    </div>
  </section>
</main>
</body>
</html>
```